Web Design for a recruitment company

Website is for a recruitment company, with a particular focus on temporary staff, trades, skilled, and unskilled labour markets. Website will consist of a home page design and separate design for additional pages. Website will be implemented as a template in SharePoint. There is a separate design project for a new logo and look colours will need to be co-ordinated.

Target Market(s)

Company executives in the construction and trades areas looking for staff. Trades people, skilled and unskilled labourers looking for work.

Industry/Entity Type

It Company

Number of Pages Required

2 page

Requirements
Must have
• Looking for Home Page design plus design for additional pages.
• .
Nice to have
• Good Crew | Good Site is the firms byline, company name is TOV Staffing. They will be in the Logo (separate project) but may also appear elsewhere in the design.
• Company values (attached file) may be reflected in the design where practical.

```html
<!DOCTYPE html>
<html lang="en">
<head>
<meta charset="utf-8">
<title>TOV Staffing – Home</title>
<link href="https://fonts.googleapis.com/css2?family=Roboto:wght@400;500;700&family=Open+Sans:wght@400;600&family=Oswald:wght@500&display=swap" rel="stylesheet">
<style>
:root{
  --red:#e8473b;
  --ink:#333333;
  --muted:#8a8a8a;
  --line:#ececec;
  --soft:#f6f6f6;
  --dark:#2b2b2b;
  --white:#ffffff;
}
*{box-sizing:border-box;margin:0;padding:0}
html,body{width:700px;height:1200px;overflow:hidden;background:var(--white)}
body{position:relative;font-family:"Open Sans",Arial,sans-serif;color:var(--ink)}
.abs{position:absolute}

.site-header{left:0;top:0;width:700px;height:64px;background:var(--white);box-shadow:0 2px 3px rgba(0,0,0,.12);z-index:2}
.brand{left:100px;top:16px;display:flex;align-items:flex-start;gap:8px}
.brand-mark{width:28px;height:28px;border-radius:50%;background:#3a3a3a;margin-top:2px}
.brand-name{font-family:"Roboto",sans-serif;font-weight:700;font-size:19px;color:#222;line-height:20px}
.brand-byline{font-size:10px;color:#333;line-height:13px;margin-top:1px}
.main-nav{left:290px;top:27px;display:flex;font-family:"Open Sans",sans-serif;font-size:10.5px;color:#555}
.main-nav span{padding:0 13px;border-left:1px solid #e2e2e2;line-height:12px}
.main-nav span:first-child{border-left:0;color:var(--red)}

.hero{left:0;top:64px;width:700px;height:302px;background:linear-gradient(100deg,#5e6e84 0%,#c9d0da 40%,#dfe3ea 55%,#3d4a5e 85%,#27313f 100%)}
.hero-arrow{width:20px;height:20px;border-radius:50%;background:rgba(40,40,40,.45);top:211px}
.hero-title{left:98px;top:245px;font-family:"Oswald",sans-serif;font-weight:500;font-size:28px;color:var(--white);letter-spacing:-.3px}

.welcome{left:100px;top:330px;width:330px;height:130px;background:var(--red);color:var(--white);padding:10px 14px}
.welcome h1{font-family:"Roboto",sans-serif;font-weight:500;font-size:18px;margin-bottom:8px}
.welcome p{font-size:6.4px;line-height:12px}
.welcome .more{display:block;margin-top:8px;font-size:6.4px}
.welcome-art{left:430px;top:330px;width:170px;height:130px;background:linear-gradient(160deg,#aebfd2,#eef1f4 60%,#d9dde2)}
.welcome-shadow{left:120px;top:460px;width:460px;height:8px;background:radial-gradient(ellipse at top,rgba(0,0,0,.18),transparent 70%)}

.section-title{left:0;width:700px;text-align:center;font-family:"Roboto",sans-serif;font-size:14px;color:#333}
.service{width:118px;height:148px;background:#fafafa;border:1px solid #f0f0f0;top:510px}
.service .photo{height:91px}
.service h3{font-family:"Roboto",sans-serif;font-weight:400;font-size:9px;color:var(--red);margin:10px 8px 6px}
.service p{font-size:6.2px;color:var(--muted);line-height:11px;margin:0 8px;text-align:justify}

.mission-title{left:0;top:683px;width:700px;text-align:center;font-family:"Roboto",sans-serif;font-size:15.5px;color:var(--red)}
.mission-sub{left:0;top:708px;width:700px;text-align:center;font-family:"Roboto",sans-serif;font-size:8.5px;color:#333}
.divider-v{left:350px;top:736px;width:1px;height:160px;background:var(--line)}
.divider-h{left:100px;top:816px;width:500px;height:1px;background:var(--line)}
.value-icon{width:48px;height:48px;border-radius:50%;background:var(--white);border:1px solid #eee;box-shadow:0 1px 3px rgba(0,0,0,.06)}
.value-num{width:17px;height:17px;border-radius:50%;background:var(--red);color:var(--white);font-size:8px;font-weight:600;text-align:center;line-height:17px;font-style:italic}
.value-num::after{content:"";position:absolute;right:-4px;top:5px;border-left:5px solid var(--red);border-top:4px solid transparent;border-bottom:4px solid transparent}
.value h4{font-family:"Roboto",sans-serif;font-weight:400;font-size:10.5px;color:#444;margin-bottom:7px}
.value p{font-size:6.4px;color:var(--muted);line-height:12px;width:130px}
.btn-more{left:298px;top:902px;width:104px;height:23px;border-radius:12px;background:var(--red);color:var(--white);font-family:"Roboto",sans-serif;font-size:8px;text-align:center;line-height:23px}

.news-photo{width:102px;height:96px;top:988px}
.news{top:986px;width:130px}
.news h3{font-family:"Roboto",sans-serif;font-weight:400;font-size:8.6px;color:#444;margin-bottom:7px}
.news .date{font-size:6.4px;color:var(--red);margin-bottom:8px}
.news p{font-size:6px;color:var(--muted);line-height:12px;text-align:justify}
.news .more{font-size:6px;color:#666;margin-top:8px}

.footer{left:0;top:1114px;width:700px;height:52px;background:var(--soft)}
.social{width:15px;height:15px;border-radius:50%;background:#9a9a9a;top:1132px}
.foot-sep{width:1px;height:34px;background:#e4e4e4;top:1123px}
.foot-text{font-size:7.6px;color:#666;line-height:13px}
.bottom-bar{left:0;top:1166px;width:700px;height:34px;background:var(--dark);color:#ddd;font-size:6.6px;text-align:center;line-height:34px}
</style>
</head>
<body>

<header class="site-header abs">
  <div class="brand abs">
    <div class="brand-mark"></div>
    <div>
      <div class="brand-name">TOV Staffing</div>
      <div class="brand-byline">Good Crew | Good Site</div>
    </div>
  </div>
  <nav class="main-nav abs"><span>Home</span><span>About Us</span><span>Our Mission</span><span>Services</span><span>Contact</span></nav>
</header>

<section class="hero abs" role="img" aria-label="Photo of business people in a meeting"></section>
<svg class="hero-arrow abs" style="left:24px" viewBox="0 0 20 20"><path d="M11.5 6 7.5 10l4 4" fill="none" stroke="#fff" stroke-width="1.6"/></svg>
<svg class="hero-arrow abs" style="left:664px;background:rgba(40,40,40,.2)" viewBox="0 0 20 20"><path d="M8.5 6l4 4-4 4" fill="none" stroke="#fff" stroke-width="1.6"/></svg>
<div class="hero-title abs">Good Crew | Good Site</div>

<div class="welcome-shadow abs"></div>
<section class="welcome abs">
  <h1>Welcome To TOV Staffing</h1>
  <p>Lorem ipsum dolor sit amet, consectetur adipiscing elit, sed do eiusmod tempor incididunt ut labore et dolore magna aliqua. Ut enim ad minim veniam, quis nostrud exercitation ullamco laboris nisi ut aliquip ex ea commodo consequat. Duis aute irure dolor in reprehenderit in voluptate velit esse cillum dolore eu fugiat nulla pariatur. Excepteur sint occaecat cupidatat non proident, sunt in culpa qui officia deserunt mollit anim id est laborum</p>
  <span class="more">Read More &gt;&gt;</span>
</section>
<div class="welcome-art abs" role="img" aria-label="Illustration of a hand releasing creative idea words into a sky"></div>

<h2 class="section-title abs" style="top:479px">Our Services</h2>
<article class="service abs" style="left:101px"><div class="photo" role="img" aria-label="Photo of a team of temporary office staff" style="background:linear-gradient(180deg,#b9bfc8,#4a5262)"></div><h3>Temporary Staff</h3><p>Lorem ipsum dolor sit amet, eiusmod tempor incididunt</p></article>
<article class="service abs" style="left:228px"><div class="photo" role="img" aria-label="Photo of workers forming a rising chart with a red arrow" style="background:linear-gradient(180deg,#dfe7ef,#8d98a6)"></div><h3>Trades</h3><p>Lorem ipsum dolor sit amet, eiusmod tempor incididunt</p></article>
<article class="service abs" style="left:355px"><div class="photo" role="img" aria-label="Photo of a businessman looking through binoculars at the sky" style="background:linear-gradient(180deg,#2f6f88,#8fb2bf)"></div><h3>Skilled</h3><p>Lorem ipsum dolor sit amet, eiusmod tempor incididunt</p></article>
<article class="service abs" style="left:481px"><div class="photo" role="img" aria-label="Photo of seated people in business attire" style="background:linear-gradient(180deg,#c7c9cc,#3b3f48)"></div><h3>Unskilled Labour Markets</h3><p>Lorem ipsum dolor sit amet, eiusmod tempor incididunt</p></article>

<h2 class="mission-title abs">OUR MISSION / VALUE</h2>
<div class="mission-sub abs">WHAT WE VALUE MOST</div>
<div class="divider-v abs"></div>
<div class="divider-h abs"></div>

<div class="value-icon abs" style="left:100px;top:751px"><svg viewBox="0 0 48 48" width="48" height="48"><circle cx="18" cy="20" r="2.5" fill="#222"/><circle cx="30" cy="20" r="2.5" fill="#222"/><path d="M13 26q11 12 22 0q-11 5-22 0z" fill="#222"/></svg></div>
<div class="value-num abs" style="left:143px;top:767px">1</div>
<div class="value abs" style="left:177px;top:755px"><h4>E | ENJOY</h4><p>We will build and maintain an enjoyable work place</p></div>

<div class="value-icon abs" style="left:402px;top:751px"><svg viewBox="0 0 48 48" width="48" height="48"><g stroke="#222" stroke-width="1.6" stroke-linecap="round"><path d="M24 13v4M24 31v4M13 24h4M31 24h4M16 16l3 3M29 29l3 3M32 16l-3 3M19 29l-3 3"/><path d="M24 24l-3-4M24 24l4-2" /></g><circle cx="24" cy="24" r="1.6" fill="#222"/></svg></div>
<div class="value-num abs" style="left:445px;top:767px">2</div>
<div class="value abs" style="left:479px;top:755px"><h4>L | LOYALTY</h4><p>We will recognise and reward loyal staff and customers</p></div>

<div class="value-icon abs" style="left:100px;top:834px"><svg viewBox="0 0 48 48" width="48" height="48"><g fill="none" stroke="#222" stroke-width="1.5"><path d="M19 24a5 5 0 1 1 10 0c0 3-2.5 4-2.5 6h-5c0-2-2.5-3-2.5-6z"/><path d="M21.5 32h5M22 34.5h4M24 13v3M15 17l2 2M33 17l-2 2M12 24h3M33 24h3"/></g></svg></div>
<div class="value-num abs" style="left:143px;top:850px">3</div>
<div class="value abs" style="left:177px;top:838px"><h4>E | ENERGY</h4><p>We will inject energy into everything we do</p></div>

<div class="value-icon abs" style="left:402px;top:834px"><svg viewBox="0 0 48 48" width="48" height="48"><g fill="none" stroke="#222" stroke-width="1.4"><circle cx="24" cy="22" r="8"/><ellipse cx="24" cy="22" rx="3.5" ry="8"/><path d="M16 22h16M17.5 18h13M17.5 26h13M24 30v4M19 35h10"/></g></svg></div>
<div class="value-num abs" style="left:445px;top:850px">4</div>
<div class="value abs" style="left:479px;top:838px"><h4>R | RELIABLE</h4><p>We will do what we say we will do</p></div>

<div class="btn-more abs">MORE INFORMATION</div>

<h2 class="section-title abs" style="top:944px">LATEST NEWS</h2>
<div class="news-photo abs" role="img" aria-label="Photo of a man working on a laptop outdoors" style="left:101px;background:linear-gradient(180deg,#9aa6b0,#5d6b52)"></div>
<article class="news abs" style="left:216px"><h3>Lorem ipsum dolor sit amet</h3><div class="date">Nov 25, 2014</div><p>Lorem ipsum dolor sit amet, consectetuer adipiscing elit, sed diam nonummy nibh euismod tincidunt ut laoreet dolore Lorem ipsum dolor sit amet, consectetuer</p><div class="more">Read More +</div></article>
<div class="news-photo abs" role="img" aria-label="Photo of a thoughtful woman surrounded by question marks" style="left:360px;background:linear-gradient(180deg,#c9c9c9,#8a8a8a)"></div>
<article class="news abs" style="left:474px"><h3>Lorem ipsum dolor sit amet</h3><div class="date">Nov 25, 2014</div><p>Lorem ipsum dolor sit amet, consectetuer adipiscing elit, sed diam nonummy nibh euismod tincidunt ut laoreet dolore Lorem ipsum dolor sit amet, consectetuer</p><div class="more">Read More +</div></article>

<footer class="footer abs"></footer>
<div class="social abs" style="left:100px"></div>
<div class="social abs" style="left:118px"></div>
<div class="social abs" style="left:136px"></div>
<div class="social abs" style="left:156px"></div>
<div class="foot-sep abs" style="left:221px"></div>
<svg class="abs" style="left:252px;top:1132px" width="18" height="16" viewBox="0 0 18 16"><path d="M2 5q7-5 14 0v2h-3V5H5v2H2z M4 8h10l1 7H3z" fill="#d6d6d6"/></svg>
<div class="foot-sep abs" style="left:274px;top:1128px;height:24px"></div>
<div class="foot-text abs" style="left:282px;top:1128px">Telephone: +1 800 555 0142<br>Email: hello@tovstaffing.com</div>
<div class="foot-sep abs" style="left:431px"></div>
<svg class="abs" style="left:460px;top:1134px" width="18" height="13" viewBox="0 0 18 13"><rect x=".5" y=".5" width="17" height="12" fill="none" stroke="#d6d6d6"/><path d="M.5.5 9 7l8.5-6.5" fill="none" stroke="#d6d6d6"/></svg>
<div class="foot-sep abs" style="left:481px;top:1128px;height:24px"></div>
<div class="foot-text abs" style="left:488px;top:1128px">412 Harbor Lane,<br>Riverton, CA 90210. United</div>

<div class="bottom-bar abs">©2013 - 2014 TOV Staffing., All Rights Reserved.</div>

</body>
</html>
```